Coffee Roaster Needs A Postcard Design

I am coffee roaster ( a home business) and I would like to create a neighborhood delivery service. Once a month I would delivery fresh roasted coffee to my neighbors. I would like to create a postcard to advertise the coffee delivery service.

Preferences: The postcard would be very simple, primarily black and white ( a little color) with visuals; fresh roasted coffee beans, delivered to the doorstep, a great cup of coffee. Simple steps, 1 2 & 3.

I have a website the postcard advertisement should flow with the site : www.brambledgebeanworks.com

Target Market(s)

Upper class residential neighborhood

Industry/Entity Type

Business

Font styles to use
Serif

Colors
f04a50

Requirements
Must have
• Images _ Coffee Beans

```html
<!DOCTYPE html>
<html lang="en">
<head>
<meta charset="utf-8">
<title>Brambledge Beanworks – Fresh Coffee Delivered</title>
<link href="https://fonts.googleapis.com/css2?family=Bebas+Neue&family=Jost:ital,wght@0,200;0,400;0,600;1,200;1,400&display=swap" rel="stylesheet">
<style>
  :root {
    --paper: #ffffff;
    --roast: #231a17;
    --ink: #1e1614;
    --accent: #f04a50;
    --cream: #ffffff;
  }
  * { box-sizing: border-box; margin: 0; padding: 0; }
  html, body { width: 1200px; height: 781px; overflow: hidden; background: var(--paper); }
  .postcard { position: relative; width: 1200px; height: 781px; font-family: "Jost", sans-serif; color: var(--ink); }

  .front { position: absolute; left: 0; top: 0; width: 597px; height: 781px; background: var(--paper); text-align: center; }
  .brand-name { position: absolute; left: 0; width: 597px; top: 36px; font-family: "Bebas Neue", sans-serif; font-weight: 400; font-size: 64px; letter-spacing: 1px; line-height: 1; }
  .rule { position: absolute; left: 38px; width: 534px; height: 4px; background: var(--ink); border-radius: 2px; }
  .rule.top { top: 111px; }
  .rule.bottom { top: 716px; }
  .intro { position: absolute; left: 0; width: 597px; top: 122px; font-size: 19px; }
  .intro strong { font-weight: 600; }

  .steps { position: absolute; left: 0; width: 597px; top: 222px; list-style: none; }
  .step { display: flex; flex-direction: column; align-items: center; }
  .step-label { font-size: 20px; line-height: 1; margin-top: 8px; }
  .operator { font-size: 30px; font-weight: 600; line-height: 1; margin: 24px 0 20px; }

  .tagline { position: absolute; left: 0; width: 597px; top: 682px; font-size: 13px; font-style: italic; }
  .site { position: absolute; left: 0; width: 597px; top: 734px; display: flex; justify-content: center; align-items: center; gap: 10px; font-size: 15px; }

  .back { position: absolute; left: 597px; top: 0; width: 603px; height: 781px; background: var(--roast); color: var(--cream); box-shadow: -10px 0 18px rgba(0,0,0,0.18); }
  .headline { position: absolute; left: 62px; top: 92px; }
  .headline .light { display: block; font-family: "Jost", sans-serif; font-weight: 200; font-style: italic; font-size: 122px; line-height: 96px; letter-spacing: 3px; }
  .headline .bold { display: block; font-family: "Bebas Neue", sans-serif; font-size: 146px; line-height: 120px; letter-spacing: 1px; }
  .headline .bold.first { margin-top: 14px; }
  .bean-cluster { position: absolute; left: 400px; top: 82px; }
  .cup-mark { position: absolute; left: 448px; top: 456px; }
</style>
</head>
<body>
<main class="postcard">
  <section class="front">
    <h1 class="brand-name">Brambledge Beanworks</h1>
    <div class="rule top"></div>
    <p class="intro">Introducing our brand new <strong>exclusive</strong> service</p>

    <ol class="steps">
      <li class="step">
        <svg width="46" height="40" viewBox="0 0 46 40" aria-hidden="true">
          <g fill="var(--ink)">
            <ellipse cx="10" cy="14" rx="5" ry="7" transform="rotate(-30 10 14)"/>
            <ellipse cx="22" cy="10" rx="5" ry="7" transform="rotate(20 22 10)"/>
            <ellipse cx="34" cy="14" rx="5" ry="7" transform="rotate(-20 34 14)"/>
            <ellipse cx="14" cy="28" rx="5" ry="7" transform="rotate(40 14 28)"/>
            <ellipse cx="27" cy="26" rx="5" ry="7" transform="rotate(-35 27 26)"/>
            <ellipse cx="38" cy="30" rx="5" ry="7" transform="rotate(25 38 30)"/>
          </g>
        </svg>
        <span class="step-label">Fresh Roasted Coffee Beans</span>
      </li>
      <li class="operator" aria-hidden="true">+</li>
      <li class="step">
        <svg width="72" height="46" viewBox="0 0 72 46" aria-hidden="true">
          <g fill="none" stroke="var(--accent)" stroke-width="3" stroke-linecap="round">
            <circle cx="15" cy="30" r="12"/>
            <circle cx="57" cy="30" r="12"/>
            <path d="M15 30 L28 14 L50 14 L57 30 M28 14 L36 30 L50 14 M24 8 L32 8 M50 14 L48 6 L54 4 M36 30 L15 30"/>
          </g>
        </svg>
        <span class="step-label">Delivered by Bike</span>
      </li>
      <li class="operator" aria-hidden="true">=</li>
      <li class="step">
        <svg width="44" height="40" viewBox="0 0 44 40" aria-hidden="true">
          <g fill="none" stroke="var(--ink)" stroke-width="1.5">
            <path d="M14 2 q-2 3 0 6 M20 2 q-2 3 0 6 M26 2 q-2 3 0 6"/>
          </g>
          <path d="M4 16 H34 Q34 34 19 36 Q4 34 4 16 Z" fill="var(--accent)"/>
          <path d="M33 20 q9 0 7 7 q-2 5 -9 5" fill="none" stroke="var(--accent)" stroke-width="3"/>
          <rect x="4" y="14" width="30" height="4" fill="var(--ink)"/>
        </svg>
        <span class="step-label">A Great Cup of Coffee</span>
      </li>
    </ol>

    <p class="tagline">Once a month get freshly roasted coffee beans delivered to your door.</p>
    <div class="rule bottom"></div>
    <p class="site">
      <svg width="22" height="22" viewBox="0 0 22 22" aria-hidden="true">
        <circle cx="11" cy="11" r="11" fill="var(--ink)"/>
        <path d="M8 5 L8 16 L10.5 13.5 L12.5 17.5 L14 16.8 L12 12.8 L15.5 12.8 Z" fill="var(--paper)"/>
      </svg>
      www.brambledgebeanworks.com
    </p>
  </section>

  <section class="back">
    <h2 class="headline">
      <span class="light">FRESH</span>
      <span class="light">COFFEE.</span>
      <span class="bold first">DELIVERED</span>
      <span class="bold">TO YOUR</span>
      <span class="bold">DOORSTEP</span>
    </h2>
    <svg class="bean-cluster" width="110" height="110" viewBox="0 0 110 110" aria-hidden="true">
      <g fill="var(--cream)" stroke="var(--roast)" stroke-width="2">
        <ellipse cx="60" cy="18" rx="9" ry="13" transform="rotate(-60 60 18)"/>
        <ellipse cx="82" cy="24" rx="9" ry="13" transform="rotate(40 82 24)"/>
        <ellipse cx="22" cy="46" rx="9" ry="13" transform="rotate(-20 22 46)"/>
        <ellipse cx="46" cy="44" rx="9" ry="13" transform="rotate(30 46 44)"/>
        <ellipse cx="70" cy="50" rx="9" ry="13" transform="rotate(-40 70 50)"/>
        <ellipse cx="94" cy="54" rx="9" ry="13" transform="rotate(15 94 54)"/>
        <ellipse cx="16" cy="74" rx="9" ry="13" transform="rotate(50 16 74)"/>
        <ellipse cx="40" cy="76" rx="9" ry="13" transform="rotate(-15 40 76)"/>
        <ellipse cx="64" cy="82" rx="9" ry="13" transform="rotate(35 64 82)"/>
        <ellipse cx="88" cy="86" rx="9" ry="13" transform="rotate(-55 88 86)"/>
      </g>
      <g fill="none" stroke="var(--roast)" stroke-width="2">
        <path d="M50 24 q10 -4 20 -10 M76 16 q4 8 12 16 M18 34 q6 12 8 24 M40 34 q6 10 12 20 M62 58 q6 -6 16 -16 M92 42 q0 12 4 24 M8 68 q8 6 16 12 M38 64 q2 12 4 24 M58 72 q6 8 12 18 M80 92 q6 -6 16 -12"/>
      </g>
    </svg>
    <svg class="cup-mark" width="96" height="70" viewBox="0 0 96 70" aria-hidden="true">
      <g fill="none" stroke="var(--cream)" stroke-width="2">
        <path d="M26 2 q-4 5 0 10 q4 5 0 10 M36 2 q-4 5 0 10 q4 5 0 10 M46 2 q-4 5 0 10 q4 5 0 10"/>
      </g>
      <path d="M2 28 H76 Q76 64 39 68 Q2 64 2 28 Z" fill="var(--cream)"/>
      <path d="M74 34 q18 -2 16 12 q-2 10 -22 12" fill="none" stroke="var(--cream)" stroke-width="5"/>
    </svg>
  </section>
</main>
</body>
</html>
```